In house, web site post, social media post, and email blast specials/promo flyer

We are looking to update our monthly specials flyer to be sent out via Bright Mailway as well as printed and handed out in office and social media and posted to our website. Please see attachments below for a sample of a previous flyer. We want it to look clean and not too busy. It should be professional looking as this is going to a higher end client that is paying cash for our services

Target Market(s)

Women and Men 35-55

Contact Information for Business Card

I am tired of our current business card and want a fresh updated look. We want something simple, clean, and modern looking.

Font styles to use
Sans Serif
Script

Colors
3377b5
34a7d8
85cae6
85abd2
cedeed
ecf7fb
eaf1f7

Requirements
Must have
• Clean lines, Sexy, appealing to the medical spa beauty industry. Our clients come to us to look and feel good.
• Content of actual specials:
• FIGHT FINE LINES AND WRINKLES-Purchase a minimum of 30 units of Lumivex and receive a complimentary Glycolic Acid Peel ($150 VALUE)
• THE SWEAT STOPS HERE-Permanently stop underarm sweat with DuraCalm treatments, starting at $1,950
• BRIGHTEN & TONE-IPL $ Beam Serenity package $3,500
• REDUCE FACE & LEG VEINS- 15% off packages
• VOLUMERA: CHEEKS & NL FOLDS-SECOND SYRINGE 25% OFF, THIRD SYRINGE $50 OFF
• BODY SCULPTING FOR ABDOMEN AND THIGHS-Blast unwanted fat with a trio of treatments! $4,799
Nice to have
• Here are some sample flyers of what we would like ours to look like
• https://www.kelomirskinspa.com/specials/
• https://brevanolaclinic.com/november-specials-2017/

```html
<!DOCTYPE html>
<html lang="en">
<head>
<meta charset="utf-8">
<title>Solenne Monthly Specials</title>
<link rel="stylesheet" href="https://fonts.googleapis.com/css2?family=Open+Sans:wght@400;600;700&family=Oswald:wght@400;500&display=swap">
<style>
  :root {
    --blue-deep: #3377b5;
    --blue-bright: #34a7d8;
    --blue-sky: #85cae6;
    --blue-steel: #85abd2;
    --blue-mist: #cedeed;
    --blue-ice: #ecf7fb;
    --blue-pale: #eaf1f7;
    --ink: #555a60;
    --ink-soft: #6d7278;
    --brand-ink: #2d6076;
    --white: #ffffff;
  }
  * { box-sizing: border-box; margin: 0; padding: 0; }
  html, body { width: 707px; height: 1200px; overflow: hidden; background: var(--white); }
  body { font-family: "Open Sans", Arial, sans-serif; color: var(--ink); position: relative; }

  .hero { position: absolute; left: 0; top: 0; width: 707px; height: 660px; }
  .hero svg { display: block; }
  .brand-name {
    position: absolute; left: 345px; top: 445px; width: 200px; text-align: center;
    font-family: "Open Sans", Arial, sans-serif; font-weight: 600; font-size: 36px;
    letter-spacing: 1px; color: var(--brand-ink);
  }

  .specials { position: absolute; left: 0; top: 690px; width: 707px; height: 190px; }
  .special { position: absolute; width: 300px; }
  .special h2 {
    font-size: 17px; font-weight: 700; color: var(--blue-bright); letter-spacing: 0.2px;
    padding-bottom: 3px; border-bottom: 2px solid #9aa3ab; display: inline-block; width: 290px;
  }
  .special p { font-size: 12.5px; line-height: 1.45; color: var(--ink-soft); margin-top: 8px; }
  .price { font-weight: 700; font-size: 19px; color: var(--blue-deep); }
  .pct { font-weight: 700; font-size: 19px; color: var(--blue-bright); }
  .lead { font-size: 18px; color: var(--ink); }
  .col-left { left: 38px; }
  .col-right { left: 424px; }
  .divider { position: absolute; left: 362px; top: 8px; width: 2px; height: 160px; background: #b9c0c6; }
  .divider::after { content: ""; position: absolute; left: -1px; top: 55px; width: 4px; height: 60px; background: #8d959c; }

  .promo-tab {
    position: absolute; left: 263px; top: 900px; width: 180px; height: 38px;
    background: var(--blue-deep); border-radius: 8px 8px 0 0;
    color: var(--white); font-family: "Open Sans", Arial, sans-serif; font-weight: 700;
    font-size: 21px; text-align: center; line-height: 38px; letter-spacing: 0.5px;
  }
  .promo-band {
    position: absolute; left: 0; top: 938px; width: 707px; height: 82px;
    background: linear-gradient(180deg, var(--blue-deep) 0%, #4b92cc 55%, var(--blue-sky) 100%);
    color: var(--white); text-align: center; font-family: "Oswald", "Arial Narrow", sans-serif;
  }
  .promo-band .line-one { font-size: 22px; font-weight: 500; padding-top: 6px; line-height: 1.2; }
  .promo-band .line-two { font-size: 33px; font-weight: 400; line-height: 1.15; letter-spacing: 0.5px; }

  .sculpt { position: absolute; left: 0; top: 1040px; width: 707px; text-align: center; }
  .sculpt h3 { font-size: 20px; font-weight: 700; color: var(--ink); letter-spacing: 0.3px; }
  .sculpt p { font-size: 19px; color: var(--blue-bright); margin-top: 4px; }

  .footer {
    position: absolute; left: 0; top: 1152px; width: 707px; height: 48px;
    background: var(--blue-steel); color: var(--white);
    display: flex; align-items: center; justify-content: center; gap: 16px; font-size: 14px;
  }
  .footer .item { display: flex; align-items: center; gap: 8px; }
  .footer .web { font-size: 17px; }
  .footer .sep { width: 2px; height: 22px; background: var(--white); }
</style>
</head>
<body>

<section class="hero">
  <svg width="707" height="660" viewBox="0 0 707 660" aria-hidden="false">
    <defs>
      <clipPath id="heroClip"><circle cx="170" cy="230" r="400"/></clipPath>
      <linearGradient id="portraitTone" x1="0" y1="0" x2="1" y2="1">
        <stop offset="0" stop-color="#f3e7d6"/>
        <stop offset="0.45" stop-color="#d9b58c"/>
        <stop offset="1" stop-color="#e9d7c6"/>
      </linearGradient>
      <linearGradient id="facialTone" x1="0" y1="0" x2="0" y2="1">
        <stop offset="0" stop-color="#e8d2c4"/>
        <stop offset="1" stop-color="#f4f1ef"/>
      </linearGradient>
    </defs>
    <g clip-path="url(#heroClip)">
      <rect x="0" y="0" width="707" height="660" fill="url(#portraitTone)" role="img" aria-label="Portrait photo of a smiling woman with long wavy blonde hair in a floral top"/>
    </g>
    <circle cx="170" cy="230" r="408" fill="none" stroke="var(--blue-deep)" stroke-width="16"/>
    <circle cx="545" cy="165" r="104" fill="var(--blue-sky)"/>
    <circle cx="545" cy="165" r="96" fill="url(#facialTone)" role="img" aria-label="Photo of a woman receiving a facial mask treatment with a towel wrap"/>
    <circle cx="445" cy="470" r="104" fill="var(--blue-mist)"/>
    <circle cx="445" cy="470" r="97" fill="var(--white)"/>
  </svg>
  <div class="brand-name">Solenne</div>
</section>

<section class="specials">
  <div class="special col-left" style="top:0;">
    <h2>FIGHT FINE LINES AND WRINKLES</h2>
    <p>Purchase a minimum of 30 units of Lumivex and<br>receive a complimentary Glycolic Acid Peel</p>
    <div class="price">($150 VALUE)</div>
  </div>
  <div class="special col-left" style="top:112px;">
    <h2>BRIGHTEN &amp; TONE-IPL</h2>
    <p>$ Beam Serenity package <span class="price">$3,500</span></p>
  </div>
  <div class="divider"></div>
  <div class="special col-right" style="top:0;">
    <h2>THE SWEAT STOPS HERE</h2>
    <p>Permanently stop underarm sweat with<br>DuraCalm treatments, starting at</p>
    <div class="price">$1,950</div>
  </div>
  <div class="special col-right" style="top:112px;">
    <h2>REDUCE FACE &amp; LEG VEINS</h2>
    <p><span class="pct">15%</span> <span class="lead">off packages</span></p>
  </div>
</section>

<div class="promo-tab">VOLUMERA</div>
<section class="promo-band">
  <div class="line-one">CHEEKS &amp; NL FOLDS-SECOND SYRINGE 25% OFF</div>
  <div class="line-two">THIRD SYRINGE $50 OFF</div>
</section>

<section class="sculpt">
  <h3>BODY SCULPTING FOR ABDOMEN AND THIGHS</h3>
  <p>Blast unwanted fat with a trio of treatments! $4,799</p>
</section>

<footer class="footer">
  <div class="item">
    <svg width="18" height="18" viewBox="0 0 18 18" aria-hidden="true">
      <circle cx="9" cy="9" r="8" fill="none" stroke="#fff" stroke-width="1.5"/>
      <path d="M9 4.2a3 3 0 0 0-3 3c0 2.3 3 5.8 3 5.8s3-3.5 3-5.8a3 3 0 0 0-3-3z" fill="#fff"/>
      <circle cx="9" cy="7.2" r="1.1" fill="var(--blue-steel)"/>
    </svg>
    <span>418 NW Alder Row, Suite 3, Portland, OR 97210</span>
  </div>
  <div class="sep"></div>
  <div class="item web">
    <svg width="18" height="18" viewBox="0 0 18 18" aria-hidden="true">
      <circle cx="9" cy="9" r="8" fill="none" stroke="#fff" stroke-width="1.5"/>
      <circle cx="9" cy="9" r="4.5" fill="none" stroke="#fff" stroke-width="1.2"/>
      <path d="M4.5 9h9M9 4.5c-1.6 1.4-1.6 7.6 0 9M9 4.5c1.6 1.4 1.6 7.6 0 9" fill="none" stroke="#fff" stroke-width="1"/>
    </svg>
    <span>www.solenneportland.com</span>
  </div>
</footer>

</body>
</html>
```